mobile app design: app provides timely Natural gas pipeline information (similar to weather, etc)

we are going to create and publish an app in all the three markets.( android, ios,windows). we have wire framed mostly all the screens. the designers are to provide the layout, design & background. The following are the most important things.

1. the app's target audience are guys working in the natural gas industry in the US.
2. the app provides the customer with latest pipeline information
3. the trial version is free and will provide information about one pipeline
4. slides 1 to 5 are trial version slides.
5. slides 6 onwards the customer chooses.
6. the final product is displayed in a grid.
7. the app will be developed using html5 and css3.
8. customer will pay per pipeline for the information. ( in app payment)
9 there are similiar ( complementary) products which provide weekly storage data at vexlo mart and quorbit app store.
10. i have attached the pdf document of the wireframe.
11.i have attached the logo
12. no name has been thought out yet.

Hi guys

I have a main question for the designer community .

1. is it possible to combine some of the pages ( screens  ) into one or two. use your gut feel. if not it is ok.

2. check out the flow, the color, the background , the font and the font size. it should be pleasing.

thanx

Tomek

Natural Gas

```html
<!DOCTYPE html>
<html lang="en">
<head>
<meta charset="utf-8">
<title>Pipelines app screens</title>
<link rel="stylesheet" href="https://fonts.googleapis.com/css2?family=Open+Sans:wght@300;400;600;700&display=swap">
<style>
:root{
  --page:#eef1f3;
  --teal:#26b5ad;
  --teal-dark:#1fa39c;
  --status:#2f2f2f;
  --tabbar:#2d2d2d;
  --content:#e7e7e7;
  --white:#ffffff;
  --text:#5a5a5a;
  --muted:#8c8c8c;
  --line:#e2e2e2;
  --grey-btn:#c4c4c4;
}
*{box-sizing:border-box;margin:0;padding:0}
html,body{width:1200px;height:1057px;overflow:hidden}
body{background:var(--page);font-family:"Open Sans",sans-serif;position:relative;color:var(--text)}
.screen{position:absolute;top:168px;width:408px;height:720px;background:var(--content);overflow:hidden;box-shadow:0 2px 10px rgba(0,0,0,.12)}
.screen--pipelines{left:117px}
.screen--add{left:675px}
.status-bar{height:22px;background:var(--status);color:#e6e6e6;font-weight:700;font-size:15px;display:flex;align-items:center;justify-content:space-between;padding:0 6px}
.status-bar .carrier,.status-bar .power{display:flex;align-items:center;gap:4px}
.app-header{height:40px;background:var(--teal);color:var(--white);font-size:20px;font-weight:300;display:flex;align-items:center;justify-content:center}
.nav-bar{height:43px;background:var(--white);display:flex;align-items:center;justify-content:space-between;padding:0 20px 0 26px;font-size:11px;color:var(--muted);border-bottom:1px solid var(--line)}
.nav-item{display:flex;align-items:center;gap:9px}
.tab-bar{position:absolute;left:0;right:0;bottom:0;height:52px;background:var(--tabbar);display:flex;align-items:center;justify-content:space-around;padding:0 50px}
.pipeline-list{position:absolute;left:44px;top:134px;width:315px;list-style:none}
.pipeline-item{height:29px;display:flex;align-items:center;font-size:11px}
.check{width:16px;height:16px;background:var(--white);border-radius:2px;margin-right:16px;display:flex;align-items:center;justify-content:center;flex:none}
.check--on{background:none}
.label{flex:1;height:17px;line-height:17px;padding-left:10px}
.pipeline-item:nth-child(odd) .label{background:var(--white)}
.scroll-track{position:absolute;width:4px;background:#d4d4d4;border-radius:2px}
.scroll-thumb{position:absolute;left:0;width:4px;background:var(--white);border-radius:2px}
.next-button{position:absolute;left:159px;top:570px;width:74px;height:74px;border-radius:50%;background:var(--grey-btn);display:flex;align-items:center;justify-content:center}
.data-table{position:absolute;left:15px;top:126px;width:367px;background:var(--white)}
.row{display:grid;grid-template-columns:99px 110px 86px 72px;height:32.8px;align-items:center;text-align:center;font-size:11px;color:var(--muted)}
.row>span{border-right:1px solid var(--line);height:100%;display:flex;align-items:center;justify-content:center;white-space:nowrap}
.row>span:last-child{border-right:0}
.row:nth-child(even){background:#f6f6f6}
.row .date{font-size:8px}
.row--head{height:36px;background:var(--teal);color:var(--white);font-weight:700;font-size:11px}
.row--head>span{border-right:0}
.actions{position:absolute;left:71px;top:610px;width:268px;height:37px;display:flex;border-radius:4px;overflow:hidden;border:1px solid #d6d6d6;font-size:12px}
.btn{flex:1;display:flex;align-items:center;justify-content:center}
.btn--primary{background:var(--teal);color:var(--white)}
.btn--secondary{background:#f2f2f2;color:#a6a6a6}
</style>
</head>
<body>

<section class="screen screen--pipelines">
  <div class="status-bar">
    <span class="carrier"><svg width="24" height="11"><rect x="0" y="7" width="3" height="4" fill="#e6e6e6"/><rect x="5" y="5" width="3" height="6" fill="#e6e6e6"/><rect x="10" y="3" width="3" height="8" fill="#e6e6e6"/><rect x="15" y="1" width="3" height="10" fill="#e6e6e6"/><rect x="20" y="0" width="3" height="11" fill="#e6e6e6"/></svg>KELO</span>
    <span class="time">10:35 AM</span>
    <span class="power"><svg width="13" height="13"><circle cx="6.5" cy="6.5" r="6" fill="#e6e6e6"/><path d="M6.5 3v3.5h3" stroke="#2f2f2f" stroke-width="1.5" fill="none"/></svg>65%<svg width="28" height="13"><rect x="1" y="1" width="23" height="11" fill="none" stroke="#e6e6e6" stroke-width="1.4"/><rect x="3" y="3" width="13" height="7" fill="#e6e6e6"/><rect x="25" y="4" width="2" height="5" fill="#e6e6e6"/></svg></span>
  </div>
  <header class="app-header">Pipelines</header>
  <nav class="nav-bar">
    <span class="nav-item"><svg width="18" height="16"><rect y="1" width="18" height="2.4" fill="#26b5ad"/><rect y="7" width="18" height="2.4" fill="#26b5ad"/><rect y="13" width="18" height="2.4" fill="#26b5ad"/></svg>Main Menu</span>
    <span class="nav-item"><svg width="20" height="20"><circle cx="10" cy="10" r="10" fill="#26b5ad"/><text x="10" y="14.5" text-anchor="middle" font-size="13" font-weight="700" fill="#fff" font-family="Open Sans,sans-serif">$</text></svg>Payment</span>
    <span class="nav-item"><svg width="20" height="20"><circle cx="10" cy="10" r="8.8" fill="none" stroke="#26b5ad" stroke-width="2"/><path d="M14.5 10H6M9.5 6.2 5.7 10l3.8 3.8" stroke="#26b5ad" stroke-width="2" fill="none"/></svg>To Trial version</span>
  </nav>

  <ul class="pipeline-list">
    <li class="pipeline-item"><span class="check check--on"><svg width="20" height="16"><path d="M1 8l6 6L19 1" stroke="#26b5ad" stroke-width="2.2" fill="none"/></svg></span><span class="label">Quillan Pipeline Company</span></li>
    <li class="pipeline-item"><span class="check"></span><span class="label">Ridgeway Express Pipeline</span></li>
    <li class="pipeline-item"><span class="check"></span><span class="label">Rubra Pipeline</span></li>
    <li class="pipeline-item"><span class="check"></span><span class="label">Sorrel Trails Pipeline</span></li>
    <li class="pipeline-item"><span class="check"></span><span class="label">Sable Natural Gas Company</span></li>
    <li class="pipeline-item"><span class="check check--on"><svg width="20" height="16"><path d="M1 8l6 6L19 1" stroke="#26b5ad" stroke-width="2.2" fill="none"/></svg></span><span class="label">Starling Central Gas Pipeline, Inc</span></li>
    <li class="pipeline-item"><span class="check"></span><span class="label">Suvera</span></li>
    <li class="pipeline-item"><span class="check check--on"><svg width="20" height="16"><path d="M1 8l6 6L19 1" stroke="#26b5ad" stroke-width="2.2" fill="none"/></svg></span><span class="label">Tenfold Gas Pipeline Company</span></li>
    <li class="pipeline-item"><span class="check"></span><span class="label">Tallis Eastern Transmission Pipeline</span></li>
    <li class="pipeline-item"><span class="check"></span><span class="label">Tarrow Gas Pipe Line Corporation</span></li>
    <li class="pipeline-item"><span class="check check--on"><svg width="20" height="16"><path d="M1 8l6 6L19 1" stroke="#26b5ad" stroke-width="2.2" fill="none"/></svg></span><span class="label">Tarrow Gas Transmission, LLC [7]</span></li>
    <li class="pipeline-item"><span class="check"></span><span class="label">Teldon-Orin Pipeline</span></li>
    <li class="pipeline-item"><span class="check"></span><span class="label">Trailmark Pipeline Company</span></li>
    <li class="pipeline-item"><span class="check"></span><span class="label">Transvale Pipeline</span></li>
  </ul>
  <div class="scroll-track" style="left:372px;top:140px;height:390px"><div class="scroll-thumb" style="top:6px;height:56px"></div></div>

  <div class="next-button"><svg width="44" height="44"><circle cx="22" cy="22" r="19" fill="none" stroke="#fff" stroke-width="3"/><path d="M11 22h20M23 13.5 31.5 22 23 30.5" stroke="#fff" stroke-width="3.2" fill="none"/></svg></div>

  <footer class="tab-bar">
    <svg width="18" height="16"><rect y="1" width="18" height="2.2" fill="#bdbdbd"/><rect y="7" width="18" height="2.2" fill="#bdbdbd"/><rect y="13" width="18" height="2.2" fill="#bdbdbd"/></svg>
    <svg width="20" height="20"><circle cx="10" cy="10" r="10" fill="#bdbdbd"/><text x="10" y="14.5" text-anchor="middle" font-size="13" font-weight="700" fill="#2d2d2d" font-family="Open Sans,sans-serif">$</text></svg>
    <svg width="20" height="20"><circle cx="10" cy="10" r="8.8" fill="none" stroke="#bdbdbd" stroke-width="2"/><path d="M14.5 10H6M9.5 6.2 5.7 10l3.8 3.8" stroke="#bdbdbd" stroke-width="2" fill="none"/></svg>
  </footer>
</section>

<section class="screen screen--add">
  <div class="status-bar">
    <span class="carrier"><svg width="24" height="11"><rect x="0" y="7" width="3" height="4" fill="#e6e6e6"/><rect x="5" y="5" width="3" height="6" fill="#e6e6e6"/><rect x="10" y="3" width="3" height="8" fill="#e6e6e6"/><rect x="15" y="1" width="3" height="10" fill="#e6e6e6"/><rect x="20" y="0" width="3" height="11" fill="#e6e6e6"/></svg>KELO</span>
    <span class="time">10:35 AM</span>
    <span class="power"><svg width="13" height="13"><circle cx="6.5" cy="6.5" r="6" fill="#e6e6e6"/><path d="M6.5 3v3.5h3" stroke="#2f2f2f" stroke-width="1.5" fill="none"/></svg>65%<svg width="28" height="13"><rect x="1" y="1" width="23" height="11" fill="none" stroke="#e6e6e6" stroke-width="1.4"/><rect x="3" y="3" width="13" height="7" fill="#e6e6e6"/><rect x="25" y="4" width="2" height="5" fill="#e6e6e6"/></svg></span>
  </div>
  <header class="app-header">Add Pipelines</header>
  <nav class="nav-bar">
    <span class="nav-item"><svg width="18" height="16"><rect y="1" width="18" height="2.4" fill="#26b5ad"/><rect y="7" width="18" height="2.4" fill="#26b5ad"/><rect y="13" width="18" height="2.4" fill="#26b5ad"/></svg>Main Menu</span>
    <span class="nav-item"><svg width="20" height="20"><circle cx="10" cy="10" r="10" fill="#26b5ad"/><text x="10" y="14.5" text-anchor="middle" font-size="13" font-weight="700" fill="#fff" font-family="Open Sans,sans-serif">$</text></svg>Payment</span>
    <span class="nav-item"><svg width="20" height="20"><circle cx="10" cy="10" r="8.8" fill="none" stroke="#26b5ad" stroke-width="2"/><path d="M14.5 10H6M9.5 6.2 5.7 10l3.8 3.8" stroke="#26b5ad" stroke-width="2" fill="none"/></svg>To Trial version</span>
  </nav>

  <div class="data-table">
    <div class="row row--head"><span>Region</span><span>Pipeline</span><span>GasDay</span><span>Date</span></div>
    <div class="row"><span>Northwest</span><span>Teldon - Orin</span><span>Data</span><span class="date">May 15, 2014</span></div>
    <div class="row"><span>Northwest</span><span>Teldon - Orin</span><span>Data</span><span class="date">May 15, 2014</span></div>
    <div class="row"><span>Northwest</span><span>Teldon - Orin</span><span>Data</span><span class="date">May 15, 2014</span></div>
    <div class="row"><span>Northwest</span><span>Teldon - Orin</span><span>Data</span><span class="date">May 15, 2014</span></div>
    <div class="row"><span>Northwest</span><span>Teldon - Orin</span><span>Data</span><span class="date">May 15, 2014</span></div>
    <div class="row"><span>Northwest</span><span>Teldon - Orin</span><span>Data</span><span class="date">May 15, 2014</span></div>
    <div class="row"><span>Northwest</span><span>Teldon - Orin</span><span>Data</span><span class="date">May 15, 2014</span></div>
    <div class="row"><span>Northwest</span><span>Teldon - Orin</span><span>Data</span><span class="date">May 15, 2014</span></div>
    <div class="row"><span>Northwest</span><span>Teldon - Orin</span><span>Data</span><span class="date">May 15, 2014</span></div>
    <div class="row"><span>Northwest</span><span>Teldon - Orin</span><span>Data</span><span class="date">May 15, 2014</span></div>
    <div class="row"><span>Northwest</span><span>Teldon - Orin</span><span>Data</span><span class="date">May 15, 2014</span></div>
    <div class="row"><span>Northwest</span><span>Teldon - Orin</span><span>Data</span><span class="date">May 15, 2014</span></div>
    <div class="row"><span>Northwest</span><span>Teldon - Orin</span><span>Data</span><span class="date">May 15, 2014</span></div>
  </div>
  <div class="scroll-track" style="left:390px;top:176px;height:390px"><div class="scroll-thumb" style="top:8px;height:56px"></div></div>

  <div class="actions">
    <span class="btn btn--primary">Add Pipelines</span>
    <span class="btn btn--secondary">Delete Pipelines</span>
  </div>

  <footer class="tab-bar">
    <svg width="18" height="16"><rect y="1" width="18" height="2.2" fill="#bdbdbd"/><rect y="7" width="18" height="2.2" fill="#bdbdbd"/><rect y="13" width="18" height="2.2" fill="#bdbdbd"/></svg>
    <svg width="20" height="20"><circle cx="10" cy="10" r="10" fill="#bdbdbd"/><text x="10" y="14.5" text-anchor="middle" font-size="13" font-weight="700" fill="#2d2d2d" font-family="Open Sans,sans-serif">$</text></svg>
    <svg width="20" height="20"><circle cx="10" cy="10" r="8.8" fill="none" stroke="#bdbdbd" stroke-width="2"/><path d="M14.5 10H6M9.5 6.2 5.7 10l3.8 3.8" stroke="#bdbdbd" stroke-width="2" fill="none"/></svg>
  </footer>
</section>

</body>
</html>
```